Nordak Modellwerk.Brenn GmbH needed a letterhead template

For English scroll down. We need a letterhead template and since we already have our logo design successfully with you, we now want to also design the letterhead with you. Down in the uploaded file you see what is important and what should definitely be seen on our template. The template should be like the homepage (www.modellwerk.brenn) held in red, blue and white. We need a letter-head submission. In the bottom in the chapter "databases uploading" you can find the most important things, did must be on the submission. The submission shoulderstand be in the colors blue, red and white like our homepage (www.modellwerk.brenn).

```html
<!DOCTYPE html>
<html lang="de">
<head>
<meta charset="utf-8">
<title>Nordak Modellwerk.Brenn GmbH – Briefpapier</title>
<link href="https://fonts.googleapis.com/css2?family=Roboto:wght@400;500;700&display=swap" rel="stylesheet">
<style>
  :root {
    --brand-blue: #1f6bb5;
    --brand-red: #d0202e;
    --text-grey: #4a4a4a;
    --paper: #fafafa;
    --backdrop: #d4d4d4;
  }
  * { margin: 0; padding: 0; box-sizing: border-box; }
  html, body {
    width: 1200px; height: 1172px; overflow: hidden;
    background: var(--backdrop);
    font-family: "Roboto", Arial, sans-serif;
  }
  .letterhead {
    position: absolute; left: 185px; top: 0;
    width: 829px; height: 1172px;
    background: var(--paper);
  }
  .sender {
    position: absolute; left: 55px; top: 63px;
    color: var(--text-grey); font-size: 11.5px; line-height: 15px;
  }
  .sender-name {
    color: var(--brand-blue); font-weight: 700; font-size: 15.5px;
    line-height: 20px; margin-bottom: 1px;
  }
  .brand {
    position: absolute; right: 52px; top: 64px;
    display: flex; align-items: center; gap: 10px;
  }
  .brand-dot {
    width: 14px; height: 14px; border-radius: 50%;
    background: var(--brand-red);
  }
  .brand-name {
    color: var(--brand-red); font-weight: 500; font-size: 31px;
    letter-spacing: 0.2px;
  }
  .footer {
    position: absolute; left: 0; top: 1082px; width: 100%;
    font-size: 10.5px; line-height: 13.5px; color: var(--text-grey);
  }
  .footer-col {
    position: absolute; top: 0;
    border-left: 1.5px solid var(--brand-red);
    padding: 3px 0 3px 12px;
  }
  .footer-col.management { left: 46px; }
  .footer-col.bank { left: 338px; }
  .footer-col.contact { left: 592px; }
  .contact-line { display: flex; align-items: center; gap: 7px; }
  .contact-line svg { width: 9px; height: 9px; fill: var(--brand-blue); flex: none; }
</style>
</head>
<body>
  <main class="letterhead">
    <header>
      <div class="sender">
        <div class="sender-name">Nordak Modellwerk.Brenn GmbH</div>
        <div>Auweg 12</div>
        <div>6174 Brennfeld, Tirol Österreich</div>
      </div>
      <div class="brand">
        <span class="brand-dot"></span>
        <span class="brand-name">Modellwerk.Brenn</span>
      </div>
    </header>

    <footer class="footer">
      <div class="footer-col management">
        <div>Geschäftsführer Dr. Lindmayr Jonas</div>
        <div>Auweg 12</div>
        <div>6174 Brennfeld, Tirol Österreich</div>
      </div>
      <div class="footer-col bank">
        <div>Alpbank 1234 &nbsp;| &nbsp;BIC: 1234</div>
        <div>IBAN: AT11 2222 3333 4444</div>
        <div>UID-Nr.: ATU123456</div>
      </div>
      <div class="footer-col contact">
        <div class="contact-line">
          <svg viewBox="0 0 10 10" aria-hidden="true"><path d="M1 3.5C1 2 2.5 1 5 1s4 1 4 2.5L7.5 4 7 3H3l-.5 1zM2.5 5h5L8.5 9h-7z"/></svg>
          <span>0800 44 55 666</span>
        </div>
        <div class="contact-line">
          <svg viewBox="0 0 10 10" aria-hidden="true"><path d="M5 .5a4.5 4.5 0 1 0 0 9 4.5 4.5 0 0 0 0-9zm0 1.2c.6.7 1 1.6 1.1 2.6H3.9C4 3.3 4.4 2.4 5 1.7zM1.8 5.6h1.9c.1.9.4 1.8 1 2.5A3.3 3.3 0 0 1 1.8 5.6zm0-1.3a3.3 3.3 0 0 1 2.9-2.5c-.6.7-.9 1.6-1 2.5zm3.2 4c-.6-.7-1-1.6-1.1-2.7h2.2C6 6.7 5.6 7.6 5 8.3zm.3-.2c.6-.7.9-1.6 1-2.5h1.9a3.3 3.3 0 0 1-2.9 2.5zm1-3.8c-.1-.9-.4-1.8-1-2.5a3.3 3.3 0 0 1 2.9 2.5z"/></svg>
          <span>www.modellwerk.brenn</span>
        </div>
        <div class="contact-line">
          <svg viewBox="0 0 10 10" aria-hidden="true"><path d="M.5 2h9v6h-9zM1.3 2.6 5 5.4l3.7-2.8z"/></svg>
          <span>contact@modellwerk.brenn</span>
        </div>
      </div>
    </footer>
  </main>
</body>
</html>
```